Velvor IT Services Business Card

Velvor IT Services are a Perth based IT Services company. We would like to incorporate our company logo (attached) and stick with the blue that is in that design. I would like a clean look design that isn't too busy, yet creates a lasting image that is instantly recognisable in the recipients mind.

Target Market(s)

The target audience is small/medium business owners.

Industry/Entity Type

Business

Font styles to use
Serif
Sans Serif

Colors

Designer to choose colors to be used in the design.

Requirements
Must have
• The design should include:
Business name: Velvor IT Services
Directors Name: Marcus Dredge
Phone Number: 0483 906 452
Email: support@velvorit.com.au
Website: www.velvorit.com.au

```html
<!DOCTYPE html>
<html lang="en">
<head>
<meta charset="utf-8">
<title>Velvor IT Services – Business Card</title>
<link rel="stylesheet" href="https://fonts.googleapis.com/css2?family=Open+Sans:ital,wght@0,400;0,600;0,700;1,700&display=swap">
<style>
  :root {
    --page: #e6e7e9;
    --card: #ffffff;
    --blue: #1a8fe3;
    --blue-light: #4cc3f5;
    --blue-deep: #1565c0;
    --ink: #2b2b2b;
    --ink-soft: #444b52;
    --rule: #c9ccd0;
  }
  * { box-sizing: border-box; margin: 0; padding: 0; }
  html, body { width: 1200px; height: 1005px; overflow: hidden; }
  body {
    background: var(--page);
    font-family: "Open Sans", Arial, sans-serif;
    color: var(--ink);
    display: flex;
    flex-direction: column;
    align-items: center;
    justify-content: center;
    gap: 38px;
  }
  .card {
    position: relative;
    width: 780px;
    height: 446px;
    background: var(--card);
    box-shadow: 0 2px 10px rgba(0,0,0,0.12);
    overflow: hidden;
  }

  /* Front */
  .card-front {
    display: flex;
    flex-direction: column;
    align-items: center;
    justify-content: center;
  }
  .brand {
    display: flex;
    align-items: center;
    gap: 14px;
  }
  .brand-dot {
    width: 34px; height: 34px;
    border-radius: 50%;
    background: var(--blue);
    flex: none;
  }
  .brand-name {
    font-size: 40px;
    font-weight: 700;
    color: var(--blue-deep);
    letter-spacing: 0.5px;
    white-space: nowrap;
  }
  .front-web {
    margin-top: 40px;
    font-size: 19px;
    color: var(--ink);
  }

  /* Back */
  .back-band { position: absolute; left: 0; top: 0; }
  .holder-name {
    position: absolute;
    left: 26px; top: 46px;
    font-size: 26px;
    font-weight: 700;
    font-style: italic;
    color: #fff;
    letter-spacing: 0.5px;
    text-transform: uppercase;
    white-space: nowrap;
  }
  .holder-role {
    position: absolute;
    left: 360px; top: 70px;
    font-size: 19px;
    font-weight: 700;
    color: var(--ink-soft);
    white-space: nowrap;
  }
  .contacts {
    position: absolute;
    left: 0; top: 138px;
    width: 400px;
    list-style: none;
  }
  .contact {
    display: flex;
    align-items: center;
    height: 62px;
  }
  .contact-icon {
    width: 90px;
    height: 100%;
    flex: none;
    display: flex;
    align-items: center;
    justify-content: center;
    border-bottom: 1px solid var(--rule);
  }
  .contact:last-child .contact-icon { border-bottom: none; }
  .contact-icon svg { width: 24px; height: 24px; fill: var(--ink); }
  .contact-text {
    padding-left: 14px;
    font-size: 17px;
    line-height: 1.3;
    color: var(--ink);
    white-space: nowrap;
  }
  .back-brand {
    position: absolute;
    right: 46px; bottom: 60px;
  }
  .back-brand .brand-name { font-size: 34px; }
  .back-brand .brand-dot { width: 30px; height: 30px; }
</style>
</head>
<body>

  <section class="card card-front" aria-label="Card front">
    <div class="brand">
      <span class="brand-dot"></span>
      <span class="brand-name">Velvor IT Services</span>
    </div>
    <p class="front-web">www.velvorit.com.au</p>
  </section>

  <section class="card card-back" aria-label="Card back">
    <svg class="back-band" width="780" height="130" viewBox="0 0 780 130">
      <defs>
        <linearGradient id="bandFill" x1="0" y1="0" x2="1" y2="0">
          <stop offset="0" stop-color="#1a8fe3"/>
          <stop offset="0.45" stop-color="#35b4f0"/>
          <stop offset="1" stop-color="#1a8fe3"/>
        </linearGradient>
      </defs>
      <path d="M0 38 H300 C322 38 328 62 352 96 H780 V110 H0 Z" fill="url(#bandFill)"/>
      <path d="M352 96 H780 V100 H355 Z" fill="#ffffff" opacity="0.35"/>
    </svg>
    <h1 class="holder-name">Marcus Dredge</h1>
    <p class="holder-role">Managing Director</p>

    <ul class="contacts">
      <li class="contact">
        <span class="contact-icon">
          <svg viewBox="0 0 24 24"><path d="M12 2a7 7 0 0 0-7 7c0 5 7 13 7 13s7-8 7-13a7 7 0 0 0-7-7zm0 9.5A2.5 2.5 0 1 1 12 6.5a2.5 2.5 0 0 1 0 5z"/></svg>
        </span>
        <span class="contact-text">Unit 7, Kestrelvale Parade<br>Perth WA</span>
      </li>
      <li class="contact">
        <span class="contact-icon">
          <svg viewBox="0 0 24 24"><path d="M6.6 10.8a15.1 15.1 0 0 0 6.6 6.6l2.2-2.2a1 1 0 0 1 1-.25 11.4 11.4 0 0 0 3.6.57 1 1 0 0 1 1 1V20a1 1 0 0 1-1 1A17 17 0 0 1 3 4a1 1 0 0 1 1-1h3.5a1 1 0 0 1 1 1c0 1.25.2 2.45.57 3.57a1 1 0 0 1-.25 1z"/></svg>
        </span>
        <span class="contact-text">0483 906 452<br>08 5550 1742</span>
      </li>
      <li class="contact">
        <span class="contact-icon">
          <svg viewBox="0 0 24 24"><path d="M2 5h20v14H2z M3.5 6.5 12 13l8.5-6.5" fill="none" stroke="#2b2b2b" stroke-width="1.8"/><path d="M2 5h20L12 12.5z"/></svg>
        </span>
        <span class="contact-text">support@velvorit.com.au</span>
      </li>
      <li class="contact">
        <span class="contact-icon">
          <svg viewBox="0 0 24 24"><g fill="none" stroke="#2b2b2b" stroke-width="1.6"><circle cx="12" cy="12" r="9.5"/><ellipse cx="12" cy="12" rx="4.2" ry="9.5"/><path d="M2.5 12h19M4 7h16M4 17h16"/></g></svg>
        </span>
        <span class="contact-text">www.velvorit.com.au</span>
      </li>
    </ul>

    <div class="brand back-brand">
      <span class="brand-dot"></span>
      <span class="brand-name">Velvor IT Services</span>
    </div>
  </section>

</body>
</html>
```